I want an upgrade / face-lift to the all the pages and sections of the current website at vorenta.net. I am a developer but not a designer.

The website layout does not need to stay the same. Only the text, buttons, links, etc, need to stay the same. Logo can also be changed or altered.

1) Header
* Logo
* Tagline - Friends of the Messianic Community in Israel
* Short explanation - Vorenta.net aggregates new links from 113 websites of the Messianic Community in Israel. Learn more
* Login button
* Language Links (or picker) - English, Hebrew, Chinese (this currently isn't on Vorenta.net)

2) Nav Bar - no dropdowns
* Newsfeed
* Israel Directory
* International Directory
* Product Directory
* Website Directory

3) Sidebar
* Text - Sign up to Vorenta.net to receive a weekly email of new articles and videos from the Messianic community in Israel.
* Sign up button
* Brixo Ads or other Ads

4) List of Newsfeed links - (this is the main content of the homepage. Note the links go to other websites. It's not blog entries)
* Image
* Link Title
* website
* author (optional)
* date
* short description of link (optional)

5) Directory (Israel, International, Product)
* Search / Filter Bar (left vertical or horizontal ???)
* title - Israel Directory
* # of results
* A-Z
Partial for each organization
* logo
* first line - Link Name
* second link - type, city, language, area
* number of views
* description

6) Website Directory - page that lists all the websites that we crawl and gather links.
* needs upgrade / facelift

7) Organization Profile Page - click on http://vorenta.net/shalev-gate-fellowship as an example.
* all details as in list of directory, plus
* Meeting details
* contact details
* Donation details
* Donation link more prominent

8) Register Page
* include all details as on http://vorenta.net/register

9) Login Page
* include all details as on http://vorenta.net/login

10) About / FAQ / Contact pages
* include all details as on http://vorenta.net/about
* include all details as on http://vorenta.net/faq
* include all details as on http://vorenta.net/contact

11) Footer
* * include all details as on as website
About | Newsfeed | Israel Directory | International Directory | Product Directory | Website Directory | Contact
©2006–2013 Vorenta.net All rights reserved
Vorenta is a Hebrew word that means "community" or "congregation"

12) Bonus - Email Newsletter Design
* I want to send out 5 -10 new newsfeed links each weeks
* It should be similar to the newsfeed page, but for e-newsletters. I read that the css must for different and tables are preferred about for email.

The following pages appear for logged in users only
13) List of Ads
14) List of Events
15) Ad Single Page
16) Event Single Page
17) Edit Ad Form
18) Edit Event Form
19) Edit Organization Form
20) Edit User Information Form

Reason: First project. I originally entered 2 days, but am extending to 10 days.

I removed the requirement to delivery HTML/CSS and I static design of all pages is acceptable to win the project.  This is my first project and I wasn't aware that PixelHarbor focuses on static design and not HTML/CSS code.

Every designer essentially used the exact same "layout" that I currently have at vorenta.net and gave it a small "facelift".  I guess my wording in the brief of the word 'facelift' was not totally accurate.  The navbar / header layout does not need to stay the same.  I would appreciate to see different options such as the navbar at the top (like www.trendolix.net) or all one color on the header (like www.gbx.net) or making the logo all white and putting it inside the blue navbar (like trendolix.net).  Just some ideas that I had.

I am willing to make the project guaranteed but most of the designs are very close to what I have now.  

Note, any ideas / graphics / images / icons that show the visitor that the website is related to Israel would be helpful.

Reason: Not enough designs received

The project is now guaranteed‎.  I hope this encourages more designers to submit and to be creative.  I look forward to seeing more designs.

I'm interested in having a background on the left and right sides for larger screens.  For an example, see http://fieldsidetally.net/

I would like to have a faded image of the Israeli flag or a creative variation of it.

This website has a background image on the right-left sides that fades as you go down

I'm looking to use the space and the right-left to give the user at a quick glance that the website deals with Israel, community, Messianic/Christian, etc.

Another style that looks good is that white/gray such as http://www.filmquillnotes.net/ and https://vestly.io/

I'm interested to see how to block out difference sections with small color variations.

Reason: some designers request that I extend since they just accepted invitation

Another design that I like.  http://gigbarn.net/

Important change.  I want the newsfeed to look like a newsfeed. Right now, it looks like a blog site.  It's not obvious that articles are from other websites in the community.  I uploaded on the brief of clipvane's feed.  It shows the a small thumbnail (16x16 or 32x32) and then user name (it my case organization name or website name) on the upper left corner above the main image. 

On the header on want to change the wording on order.  

Top row -
Vorenta (logo in big) means community in Hebrew (in small letters) 

Next row (different background color)
The Messianic Community in Israel

Next row (different background color and smaller font)
Vorenta.net aggregates new links from 100+ websites of the Messianic Community in Israel. Learn more

I uploaded a jpg file with a new header rather than what is currently on vorenta.net

Target Market(s)

Christian around the world who love Israel

Industry/Entity Type

Events

Requirements
Must have
• responsive design to be readable on mobile devices
white / gray / blue theme
Zapto-style / portal website
Nice to have
• Bootstrap 3 of Foundation
Flat-UI (also not necessary, but I like it)
Graphics, icons, etcs, related to Israel
Passion, excellence, effort and attention to details :-)
Should not have
• dark background
too much fanciness or animations

```html
<!DOCTYPE html>
<html lang="en">
<head>
<meta charset="utf-8">
<title>Vorenta.net – Latest Newsfeed</title>
<link rel="stylesheet" href="https://fonts.googleapis.com/css2?family=Source+Sans+3:wght@300;400;600;700&display=swap">
<style>
:root{
  --blue:#1c4fb8;
  --blue-dark:#143c95;
  --blue-light:#2f67d6;
  --link:#1a55c0;
  --text:#3a3a3a;
  --muted:#666;
  --topbar:#f2f2f2;
  --orange:#f68b1f;
  --gold-top:#ffc726;
  --gold-bottom:#f9a90d;
  --rule:#e3e3e3;
  --footer:#262626;
  --footer-dark:#1a1a1a;
}
*{box-sizing:border-box;margin:0;padding:0}
html,body{width:948px;height:1200px;overflow:hidden}
body{font-family:"Source Sans 3",Arial,sans-serif;color:var(--text);background:#fff;position:relative}
a{color:var(--link);text-decoration:none}

.topbar{height:40px;background:var(--topbar);display:flex;align-items:center;justify-content:center;gap:20px;font-size:14px;color:#777;font-weight:300}
.topbar .learn{background:var(--orange);color:#fff;font-size:10px;padding:5px 13px;border-radius:2px;font-weight:600;letter-spacing:.3px}

.header{position:absolute;top:62px;left:52px;right:52px;height:36px;display:flex;align-items:center}
.logo{font-size:30px;font-weight:700;color:var(--blue);letter-spacing:-.3px}
.tagline{margin-left:48px;font-size:18px;font-weight:400;color:#333}
.lang{margin-left:auto;display:flex;align-items:center;gap:9px;font-size:13px;color:#444}
.lang .picker{border:1px solid #ccc;background:linear-gradient(#fafafa,#e8e8e8);padding:4px 10px;font-size:13px;border-radius:2px}
.login{margin-left:15px;background:linear-gradient(var(--blue-light),var(--blue));color:#fff;font-size:13px;padding:6px 21px;border-radius:2px}

.nav{position:absolute;top:119px;left:51px;width:844px;height:46px;background:linear-gradient(var(--blue-light),var(--blue-dark));border-radius:3px;display:flex}
.nav a{color:#fff;font-size:16px;display:flex;align-items:center;padding:0 19px;border-right:1px solid rgba(255,255,255,.22)}
.nav a:first-child{padding-left:36px}
.nav a:last-child{border-right:none}

.main{position:absolute;top:200px;left:51px;width:595px}
.main h1{font-size:23px;font-weight:400;color:#222;line-height:28px;margin-bottom:13px}
.item{display:flex;gap:19px;height:153px;padding-top:22px;border-bottom:1px solid var(--rule)}
.item:first-of-type{height:131px;padding-top:0}
.item:last-of-type{border-bottom:none}
.thumb{width:160px;height:110px;flex:none;border-radius:2px}
.t1{background:linear-gradient(120deg,#d9e4ea,#8ea9c2 60%,#c9b49a)}
.t2{background:linear-gradient(120deg,#d7b79c,#8f7767 55%,#cbd2d8)}
.t3{background:linear-gradient(120deg,#c8b8a6,#e8ecf2 55%,#4d7fd0)}
.t4{background:linear-gradient(120deg,#5a4a34,#c3472f 50%,#2e2a24)}
.t5{background:linear-gradient(120deg,#78818a,#cfd6dc 55%,#596470)}
.body h2{font-size:16.5px;font-weight:400;color:var(--link);line-height:20px;margin-top:-2px;margin-bottom:3px}
.body p{font-size:10.5px;line-height:18px;color:var(--muted);font-weight:300}
.body .site{font-size:12.5px;margin-top:3px;display:block}
.body .meta{font-size:10.5px;color:var(--link);margin-top:3px}
.body .meta span{color:#999;margin:0 4px}

.pager{position:absolute;top:1000px;left:219px;display:flex;gap:9px}
.pager a{background:linear-gradient(#3e6fd0,var(--blue-dark));color:#fff;font-size:10px;font-weight:600;height:19px;min-width:20px;padding:0 6px;display:flex;align-items:center;justify-content:center;border-bottom:2px solid #0f2e78}
.pager .wide{padding:0 10px}

.sidebar{position:absolute;top:188px;left:677px;width:219px}
.signup{height:162px;background:linear-gradient(var(--gold-top),var(--gold-bottom));border:1px solid #e99b00;text-align:center;padding-top:24px}
.signup h3{font-size:16.5px;font-weight:400;color:#222;line-height:20px}
.signup p{font-size:10.7px;line-height:18px;color:#333;margin:0 14px;font-weight:300}
.signup .btn{display:inline-block;margin-top:9px;background:#111;color:#fff;font-size:13px;padding:4px 14px;border-radius:3px}
.ad{width:216px;margin-top:13px;border-radius:2px}
.ad1{height:164px;background:linear-gradient(#3a3f8f,#1d2a7a 35%,#e7e9f2 35%,#2649a6)}
.ad2{height:141px;background:#2d3444;margin-top:12px}
.ad3{height:163px;background:linear-gradient(#cfe2f2 0%,#9dc1e3 58%,#1d3a7c 58%,#132a63);margin-top:13px}

.footer{position:absolute;top:1071px;left:0;width:948px;height:129px;background:linear-gradient(var(--footer),var(--footer-dark));border-top:3px solid #1d3f8f}
.footer nav{margin:32px 0 0 59px;font-size:13.5px;color:#eee}
.footer nav a{color:#fff}
.footer nav span{margin:0 5px;color:#aaa}
.footer small{display:block;margin:9px 0 0 57px;font-size:11px;color:#aaa;font-weight:300}
</style>
</head>
<body>
<div class="topbar">Vorenta.net aggregates new links from 113 websites of the Messianic Community in Israel <a class="learn" href="#">LEARN MORE</a></div>

<header class="header">
  <div class="logo">Vorenta.net</div>
  <div class="tagline">Friends of the Messianic Community in Israel</div>
  <div class="lang">Language <span class="picker">English ▾</span></div>
  <a class="login" href="#">LOGIN</a>
</header>

<nav class="nav">
  <a href="#">Newsfeed</a><a href="#">Israel Directory</a><a href="#">International Directory</a><a href="#">Product Directory</a><a href="#">Website Directory</a>
</nav>

<main class="main">
  <h1>Latest Newsfeed</h1>
  <article class="item"><div class="thumb t1" role="img" aria-label="Photo of a woman presenting to a meeting"></div><div class="body"><h2>Harvest Watch Prayer Points</h2><p>Duis tincidunt lectus quis dui viverra vestibulum. Suspendisse vulputate aliquam dui. Nulla elementum dui ut augue. Aliquam vehicula mi at mauris. Maecenas placerat, nisl at consequat rhoncus, sem nunc gravida</p><a class="site" href="#">Website: tovlightnotes.net</a><div class="meta">By Author Name<span>|</span>14 September 2013</div></div></article>
  <article class="item"><div class="thumb t2" role="img" aria-label="Photo of a group of smiling colleagues"></div><div class="body"><h2>Class aptent taciti sociosqu ad litora</h2><p>Duis tincidunt lectus quis dui viverra vestibulum. Suspendisse vulputate aliquam dui. Nulla elementum dui ut augue. Aliquam vehicula mi at mauris. Maecenas placerat, nisl at consequat rhoncus, sem nunc gravida</p><a class="site" href="#">Website: tovlightnotes.net</a><div class="meta">By Author Name<span>|</span>14 September 2013</div></div></article>
  <article class="item"><div class="thumb t3" role="img" aria-label="Photo of hands reviewing a chart on a tablet"></div><div class="body"><h2>Phasellus felis dolor scelerisque</h2><p>Duis tincidunt lectus quis dui viverra vestibulum. Suspendisse vulputate aliquam dui. Nulla elementum dui ut augue. Aliquam vehicula mi at mauris. Maecenas placerat, nisl at consequat rhoncus, sem nunc gravida</p><a class="site" href="#">Website: tovlightnotes.net</a><div class="meta">By Author Name<span>|</span>14 September 2013</div></div></article>
  <article class="item"><div class="thumb t4" role="img" aria-label="Photo of two men in a shop"></div><div class="body"><h2>Lorem ipsum dolor sit amet consectetuer</h2><p>Duis tincidunt lectus quis dui viverra vestibulum. Suspendisse vulputate aliquam dui. Nulla elementum dui ut augue. Aliquam vehicula mi at mauris. Maecenas placerat, nisl at consequat rhoncus, sem nunc gravida</p><a class="site" href="#">Website: tovlightnotes.net</a><div class="meta">By Author Name<span>|</span>14 September 2013</div></div></article>
  <article class="item"><div class="thumb t5" role="img" aria-label="Photo of office workers at a laptop"></div><div class="body"><h2>Mauris vel lacus vitae felis vestibulum</h2><p>Duis tincidunt lectus quis dui viverra vestibulum. Suspendisse vulputate aliquam dui. Nulla elementum dui ut augue. Aliquam vehicula mi at mauris. Maecenas placerat, nisl at consequat rhoncus, sem nunc gravida</p><a class="site" href="#">Website: tovlightnotes.net</a><div class="meta">By Author Name<span>|</span>14 September 2013</div></div></article>
</main>

<div class="pager">
  <a class="wide" href="#">Prev</a><a href="#">1</a><a href="#">2</a><a href="#">3</a><a href="#">4</a><a href="#">5</a><a href="#">6</a><a href="#">…</a><a href="#">22</a><a class="wide" href="#">Next</a>
</div>

<aside class="sidebar">
  <div class="signup">
    <h3>Sign up to Vorenta.net</h3>
    <p>to receive a weekly email of new articles and videos from the Messianic community in Israel</p>
    <a class="btn" href="#">Sign Up</a>
  </div>
  <div class="ad ad1" role="img" aria-label="Advertisement for sports trading cards"></div>
  <div class="ad ad2" role="img" aria-label="Advertisement for a burger restaurant"></div>
  <div class="ad ad3" role="img" aria-label="Advertisement for a shopping spree contest"></div>
</aside>

<footer class="footer">
  <nav><a href="#">About</a><span>|</span><a href="#">Newsfeed</a><span>|</span><a href="#">Israel Directory</a><span>|</span><a href="#">International Directory</a><span>|</span><a href="#">Product Directory</a><span>|</span><a href="#">Website Directory</a><span>|</span><a href="#">Contact</a></nav>
  <small>© 2013 Company Name.&nbsp; All right reserved.&nbsp; Term of Use</small>
</footer>
</body>
</html>
```